Flyer Design Project

*Update* Would also be interested to see designs in landscape format too.
My company is Brenwick Van Hire Limited. A self drive van hire company based in Essex.
I need a double sided A5 flyer design to target new business customers both small and large. The flyer will be printed on 350-400gsm.
Our website is www.brenwickvanhire.example this will give you an idea of our colour scheme.
The purpose of the flyer is to make companies aware of our business and what we offer and to ideally either make contact with us immediatly or at least retain the flyer so that they use us in future. Our aim is that when they require van hire they think of us first.
In terms of design it needs to be proffessional, eye catching, informative and memorable.
I would like the 4 main van types we supply to be on the leaflet. ideally side views. Probably stock images with our graphics placed on them. I'm sure as a designer you will have a fair idea of what I'm talking about. The van types are Mercer link, Mercer SWB, Mercer LWB high roof and Mercer luton.
Our facebook page may also help (pictures of some of our vans are here)...
http://www.facebook.example/pages/Brenwick-Van-Hire/508273619402
Ideally it will include the following. The layout of the content however I am happy to leave to the designer...
(title) Low cost business van hire
Throughout Essex and Herts including Harlow, Epping, Hoddesdon, Bishops Stortford and Hertford
We have vans in all sizes including Luton tail lifts for short and long term rental on flexible terms for any purpose at very competitive prices.
Open 7 days
Short or long term rental on daily, weekly or monthly payment terms
No charges for additional drivers
Unlimited mileage allowance
24/7 online booking facility
Account facilities available
Secure customer parking
Out of hours drop off facility
(maybe use tick boxes for the above?)
When you need a van for business purposes give Brenwick a call first.
We supply vans to businesses throughout Herts and Essex from large blue chip multinationals to small self employed tradesman. We understand the requirements of business customers and provide a low cost, flexible, efficient van hire solution regardless of the size of your business.
We’re cheaper than the rest
We regularly search the market to ensure our pricing is always competitive. It's important to us to give you excellent value for money. We operate a clear pricing structure with no hidden extras. Call us now and let us give you a quote.
Short or long term van hire
We can supply vans according to your needs from just a single days rental to long term contract rental for 1 month, 6 months, a whole year or more.
Committed to Customer service
We take customer service very seriously. We want you to be delighted each and every time you use us. That’s why We’ll always go out of our way to give you a first class service.
The longer you hire the cheaper it gets with discounts of up to 70% on our daily rental rates. (maybe in speech type bubble or highlighted in some way?)
Flyer needs:
Map of our location and address
- Finding us is easy, we're located in the foxmead industrial estate in Harlow
42 Tanwell Court
Harlow
Essex
CM17 2QT
Telephone number
0800 06 317 94
Website address
www.brenwickvanhire.example
Logo
attached
Testimonial?
Can supply
www.brenwickvanhire.example
0800 06 317 94

```html
<!DOCTYPE html>
<html lang="en">
<head>
<meta charset="utf-8">
<title>Brenwick Van Hire – Flyer</title>
<link rel="stylesheet" href="https://fonts.googleapis.com/css2?family=Arimo:wght@400;700&display=swap">
<style>
  :root {
    --green: #8cb53b;
    --green-dark: #7aa22e;
    --grey-heading: #7a7a7a;
    --grey-address: #8a8a8a;
    --ring: #dcdcdc;
    --ink: #111111;
    --paper: #ffffff;
    --contact-text: #eef4e0;
    --map-base: #efe9df;
    --van-base: #e9ecef;
  }
  * { box-sizing: border-box; margin: 0; padding: 0; }
  html, body { width: 1200px; height: 846px; overflow: hidden; background: var(--paper); }
  body { font-family: "Arimo", Arial, sans-serif; color: var(--ink); }

  .flyer { position: relative; width: 1200px; height: 846px; overflow: hidden; background: var(--paper); }

  .contact-shape { position: absolute; inset: 0; }

  .brand { position: absolute; left: 44px; top: 92px; display: flex; align-items: center; gap: 18px; }
  .brand-dot { width: 58px; height: 58px; border-radius: 50%; background: var(--green); }
  .brand-name { font-size: 58px; font-weight: 700; color: var(--green); letter-spacing: -1px; line-height: 1; }

  .location-intro { position: absolute; left: 40px; top: 242px; width: 560px; color: var(--green); font-weight: 700; font-size: 20px; line-height: 1.3; }
  .address { position: absolute; left: 40px; top: 294px; color: var(--grey-address); font-weight: 700; font-size: 15.5px; line-height: 1.3; font-style: normal; }

  .van-photo { position: absolute; left: 374px; top: 285px; width: 200px; height: 100px; border-radius: 10px; background: linear-gradient(180deg, var(--van-base), #cfd4d9); }
  .map { position: absolute; left: 29px; top: 395px; width: 573px; height: 410px; background: linear-gradient(135deg, var(--map-base), #e3ddd0); }

  .info { position: absolute; left: 649px; width: 500px; }
  .info h2 { color: var(--grey-heading); font-weight: 700; line-height: 1.1; }
  .info p { font-size: 17.4px; line-height: 1.2; }
  .info-price { top: 44px; }
  .info-price h2 { font-size: 33px; letter-spacing: -0.5px; margin-bottom: 2px; }
  .info-term { top: 226px; }
  .info-service { top: 359px; }
  .info-term h2, .info-service h2 { font-size: 24px; margin-bottom: 3px; }

  .discount { position: absolute; left: 649px; top: 503px; width: 510px; color: var(--green); font-weight: 700; font-size: 20px; line-height: 1.32; }

  .contact { position: absolute; left: 769px; top: 690px; color: var(--contact-text); }
  .contact h2 { font-size: 25px; font-weight: 700; margin-left: 69px; margin-bottom: 22px; letter-spacing: 0.3px; }
  .contact p { font-size: 19px; line-height: 1.1; }
</style>
</head>
<body>
<main class="flyer">
  <svg class="contact-shape" width="1200" height="846" viewBox="0 0 1200 846" aria-hidden="true">
    <ellipse cx="1117" cy="1016" rx="510" ry="394" fill="var(--ring)"/>
    <ellipse cx="1117" cy="1016" rx="500" ry="384" fill="var(--paper)"/>
    <ellipse cx="1117" cy="1016" rx="493" ry="377" fill="var(--green)"/>
  </svg>

  <header class="brand">
    <span class="brand-dot"></span>
    <span class="brand-name">Brenwick Van Hire</span>
  </header>

  <p class="location-intro">Finding us is easy, we're located in the foxmead industrial estate in Harlow</p>
  <address class="address">42 Tanwell Court<br>Harlow<br>Essex<br>CM17 2QT</address>

  <div class="van-photo" role="img" aria-label="Side view photo of a white Brenwick branded small van"></div>
  <div class="map" role="img" aria-label="Street map of Harlow marking the Brenwick Van Hire location"></div>

  <section class="info info-price">
    <h2>We’re cheaper than the rest!</h2>
    <p>We regularly search the market to ensure our pricing is always competitive. It's important to us to give you excellent value for money. We operate a clear pricing structure with no hidden extras. Call us now and let us give you a quote.</p>
  </section>

  <section class="info info-term">
    <h2>Short or long term van hire</h2>
    <p>We can supply vans according to your needs from just a single days rental to long term contract rental for 1 month, 6 months, a whole year or more.</p>
  </section>

  <section class="info info-service">
    <h2>Committed to Customer service</h2>
    <p>We take customer service very seriously. We want you to be delighted each and every time you use us. That’s why We’ll always go out of our way to give you a first class service.</p>
  </section>

  <p class="discount">The longer you hire the cheaper it gets with discounts of up to 70% on our daily rental rates.</p>

  <section class="contact">
    <h2>CONTACT US!</h2>
    <p>Telephone Number:&nbsp; 0800 06 317 94</p>
    <p>Website: www.brenwickvanhire.example</p>
  </section>
</main>
</body>
</html>
```